Telecommunications/Power civil contractor needs business card design

Were a new telecommunications/power underground civil contractor that is looking for a new business card design. Our company colours are silver or grey and orange. Feel free to use the white background logo or the black background logo.

Target Market(s)

Local contractors, utility companies, private sector mining/energy companies, developers.

Industry/Entity Type

Telecommunications

Contact Information for Business Card

Each card will need the following info:
Persons name:
Title:
E-mail:
Phone number:
Shop Address:
Mailing Address:

Requirements
Must have
• Each card will need the following info:
• Persons name:
• Title:
• E-mail:
• Phone number:
• Shop Address:
• Mailing Address:

```html
<!DOCTYPE html>
<html lang="en">
<head>
<meta charset="utf-8">
<title>Tarn Line Contracting Inc — Business Card</title>
<link rel="stylesheet" href="https://fonts.googleapis.com/css2?family=Open+Sans:wght@400;700&display=swap">
<style>
  :root {
    --orange: #f15a24;
    --grey-dark: #6d6e71;
    --grey-mid: #9a9b9e;
    --grey-light: #d4d5d7;
    --white: #ffffff;
    --backdrop: #2b2b2d;
    --card-shadow: rgba(0, 0, 0, 0.45);
  }
  * { box-sizing: border-box; margin: 0; padding: 0; }
  html, body {
    width: 1200px;
    height: 716px;
    overflow: hidden;
    background: var(--backdrop);
    font-family: "Open Sans", Arial, sans-serif;
  }
  .stage {
    position: relative;
    width: 1200px;
    height: 716px;
  }
  .card {
    position: absolute;
    top: 208px;
    width: 525px;
    height: 300px;
    background: var(--white);
    overflow: hidden;
    box-shadow: 0 10px 30px var(--card-shadow);
  }
  .card--front { left: 50px; }
  .card--back { left: 625px; }

  .front-shapes {
    position: absolute;
    inset: 0;
    width: 100%;
    height: 100%;
  }

  .brand {
    position: absolute;
    left: 28px;
    top: 30px;
    display: flex;
    align-items: center;
    gap: 10px;
  }
  .brand__dot {
    width: 30px;
    height: 30px;
    border-radius: 50%;
    background: var(--orange);
  }
  .brand__name {
    font-weight: 700;
    font-size: 15px;
    line-height: 1.15;
    color: var(--orange);
    text-transform: uppercase;
    letter-spacing: 0.02em;
  }

  .contact {
    position: absolute;
    right: 26px;
    top: 62px;
    text-align: right;
    color: var(--white);
    font-size: 12.5px;
    line-height: 1.4;
  }
  .contact__name {
    font-weight: 700;
    font-size: 16px;
    line-height: 1.2;
  }
  .contact__title {
    font-size: 14px;
    margin-bottom: 18px;
  }
  .contact__address { margin-bottom: 16px; }
  .contact__line {
    display: flex;
    justify-content: flex-end;
    align-items: center;
    gap: 6px;
  }
  .contact__icon {
    width: 13px;
    height: 13px;
    flex: none;
  }

  .back-brand {
    position: absolute;
    inset: 0;
    display: flex;
    flex-direction: column;
    align-items: center;
    justify-content: center;
    gap: 14px;
  }
  .back-brand__dot {
    width: 78px;
    height: 78px;
    border-radius: 50%;
    border: 6px solid var(--orange);
  }
  .back-brand__name {
    font-weight: 700;
    font-size: 18px;
    color: var(--orange);
    text-transform: uppercase;
    letter-spacing: 0.04em;
  }
</style>
</head>
<body>
<main class="stage">

  <section class="card card--front" aria-label="Business card front">
    <svg class="front-shapes" viewBox="0 0 525 300" preserveAspectRatio="none" aria-hidden="true">
      <defs>
        <linearGradient id="silver-band" x1="0" y1="1" x2="1" y2="0">
          <stop offset="0" stop-color="#58595b"/>
          <stop offset="0.5" stop-color="#a7a9ac"/>
          <stop offset="1" stop-color="#e6e7e8"/>
        </linearGradient>
      </defs>
      <path d="M140 300 C190 110 340 22 525 12 L525 44 C360 52 232 140 188 300 Z" fill="url(#silver-band)"/>
      <path d="M188 300 C232 140 360 52 525 44 L525 300 Z" fill="var(--orange)"/>
    </svg>

    <div class="brand">
      <span class="brand__dot" aria-hidden="true"></span>
      <span class="brand__name">Tarn Line<br>Contracting Inc</span>
    </div>

    <div class="contact">
      <p class="contact__name">Corin Ashby</p>
      <p class="contact__title">Managing Director</p>
      <p class="contact__address">N. 14 Alder Road,<br>Suite 200, Fairview, WA 55501</p>
      <p class="contact__line">555.010.2040
        <svg class="contact__icon" viewBox="0 0 14 14" aria-hidden="true">
          <circle cx="7" cy="7" r="6.5" fill="var(--white)"/>
          <path d="M4.3 3.6 L5.6 3.4 L6.3 5.2 L5.5 5.9 C5.9 6.9 6.6 7.7 7.6 8.2 L8.3 7.4 L10 8.1 L9.8 9.4 C7 9.6 4.2 6.7 4.3 3.6 Z" fill="var(--orange)"/>
        </svg>
      </p>
      <p class="contact__line">info@tarnlinecontracting.com
        <svg class="contact__icon" viewBox="0 0 14 14" aria-hidden="true">
          <circle cx="7" cy="7" r="6.5" fill="var(--white)"/>
          <rect x="3.5" y="4.6" width="7" height="4.8" fill="none" stroke="var(--orange)" stroke-width="1"/>
          <path d="M3.5 4.6 L7 7.4 L10.5 4.6" fill="none" stroke="var(--orange)" stroke-width="1"/>
        </svg>
      </p>
    </div>
  </section>

  <section class="card card--back" aria-label="Business card back">
    <div class="back-brand">
      <span class="back-brand__dot" aria-hidden="true"></span>
      <span class="back-brand__name">Tarn Line Contracting Inc</span>
    </div>
  </section>

</main>
</body>
</html>
```